Designer and consultant for professionals/businesses and manufacturers in the kitchen and bath in...

I have 30 years of design experience, and 19 of those years within the marketing team of a national cabinet manufacturer. This role gave me the opportunity to consult and design for kitchen/bath businesses, from boutique to multi-store national scale. My services include layout and spatial planning, individual display design, and product design for cabinet manufacturers. From showrooms, to trade shows to integrated design collections. I would like to see designs that convey professionalism, as well as an appeal to the creative designer mind!

Target Market(s)

Kitchen and bath dealers, as well as mid-scale multi-store home centers. Cabinet manufacturers, Trade Show agencies.

Industry/Entity Type

Kitchen

Contact Information for Business Card

Serving Kitchen and Bath Businesses

Logo Text

MT (initials for business name)

Font styles to use
Serif
Sans Serif
Decorative

Colors
e34197

Requirements
Must have
• Marlowe Tenbury Design and Consulting, Inc. (business name)
• marlowe@mtvorplan.com (email)
• 608-241-7789 (phone)
• mtvorplan.com (website)
Nice to have
• Inclusions of geometric shapes; particularly a 30/15 degree triangle and circle(s)
• 2 colors
Should not have
• Not too artsy!

```html
<!DOCTYPE html>
<html lang="en">
<head>
<meta charset="utf-8">
<title>Marlowe Tenbury – Business Card</title>
<link rel="stylesheet" href="https://fonts.googleapis.com/css2?family=Cinzel:wght@500&family=Montserrat:wght@400;500&display=swap">
<style>
  :root {
    --bg: #141618;
    --card: #22272b;
    --card-edge: #2b3135;
    --blue: #2fa8e0;
    --white: #eef0f2;
    --muted: #c9ced2;
  }
  * { margin: 0; padding: 0; box-sizing: border-box; }
  html, body { width: 1200px; height: 800px; overflow: hidden; background: var(--bg); }
  .stage {
    width: 1200px; height: 800px;
    display: flex; align-items: center; justify-content: center; gap: 40px;
  }
  .card {
    position: relative;
    width: 540px; height: 309px;
    background: var(--card);
    border-radius: 18px;
    box-shadow: 0 18px 40px rgba(0,0,0,.55), inset 0 0 0 1px var(--card-edge);
    overflow: hidden;
  }
  /* front */
  .front { display: flex; flex-direction: column; align-items: center; justify-content: center; }
  .front .mark { width: 118px; height: 118px; border: 4px solid var(--blue); border-radius: 50%; margin-bottom: 26px; }
  .wordmark {
    font-family: "Cinzel", serif; font-weight: 500;
    font-size: 27px; letter-spacing: 4px; color: var(--white); text-transform: uppercase;
  }
  .tagline {
    margin-top: 8px;
    font-family: "Montserrat", sans-serif; font-weight: 400;
    font-size: 10.5px; letter-spacing: 4.2px; color: var(--blue); text-transform: uppercase;
  }
  /* back */
  .back { display: flex; align-items: center; }
  .back .emblem {
    width: 170px; height: 170px; margin-left: 52px; flex: none;
    border: 5px solid var(--blue); border-radius: 50%;
    display: flex; align-items: center; justify-content: center; text-align: center;
    font-family: "Cinzel", serif; font-weight: 500; font-size: 19px; line-height: 1.35;
    letter-spacing: 2px; color: var(--white); text-transform: uppercase;
  }
  .back .ghost {
    position: absolute; right: -70px; top: -40px;
    width: 300px; height: 300px; border: 28px solid rgba(255,255,255,.035); border-radius: 50%;
  }
  .divider { width: 1px; height: 150px; background: var(--blue); opacity: .7; margin: 0 34px 0 40px; flex: none; }
  .details { position: relative; }
  .person {
    font-family: "Cinzel", serif; font-weight: 500; font-size: 20px; letter-spacing: 2.5px;
    color: var(--white); text-transform: uppercase;
  }
  .person .surname { color: var(--blue); }
  .role { font-family: "Montserrat", sans-serif; font-size: 12px; color: var(--muted); margin-top: 2px; }
  .contacts { list-style: none; margin-top: 22px; }
  .contacts li {
    display: flex; align-items: center; gap: 9px; margin-bottom: 7px;
    font-family: "Montserrat", sans-serif; font-size: 12px; color: var(--white);
  }
  .contacts svg { width: 16px; height: 16px; flex: none; }
</style>
</head>
<body>
<main class="stage">
  <section class="card front" aria-label="Card front">
    <div class="mark" aria-hidden="true"></div>
    <h1 class="wordmark">Marlowe Tenbury</h1>
    <p class="tagline">Design and Consulting, Inc.</p>
  </section>

  <section class="card back" aria-label="Card back">
    <div class="ghost" aria-hidden="true"></div>
    <div class="emblem">Marlowe<br>Tenbury</div>
    <div class="divider" aria-hidden="true"></div>
    <div class="details">
      <p class="person">Marlowe <span class="surname">Tenbury</span></p>
      <p class="role">Managing Director</p>
      <ul class="contacts">
        <li>
          <svg viewBox="0 0 16 16" aria-hidden="true"><circle cx="8" cy="8" r="8" fill="#2fa8e0"/><rect x="4" y="5" width="8" height="6" rx="1" fill="none" stroke="#22272b" stroke-width="1.2"/><path d="M4 5.5l4 3 4-3" fill="none" stroke="#22272b" stroke-width="1.2"/></svg>
          marlowe@mtvorplan.com
        </li>
        <li>
          <svg viewBox="0 0 16 16" aria-hidden="true"><circle cx="8" cy="8" r="8" fill="#2fa8e0"/><path d="M5.5 4.5l1.5 0 .7 2-1 .8a5 5 0 0 0 2 2l.8-1 2 .7v1.5c0 .5-.5.8-1 .8A6 6 0 0 1 4.7 5.5c0-.5.3-1 .8-1z" fill="#22272b"/></svg>
          608-241-7789
        </li>
        <li>
          <svg viewBox="0 0 16 16" aria-hidden="true"><circle cx="8" cy="8" r="8" fill="#2fa8e0"/><circle cx="8" cy="8" r="4" fill="none" stroke="#22272b" stroke-width="1.1"/><path d="M4 8h8M8 4c-2 2.5-2 5.5 0 8M8 4c2 2.5 2 5.5 0 8" fill="none" stroke="#22272b" stroke-width="1"/></svg>
          mtvorplan.com
        </li>
      </ul>
    </div>
  </section>
</main>
</body>
</html>
```